New Business and Accounting Software need a Graphics

We need graphic designs for a Business and Accounting Software that has 3 products and several modules.
Each product and module has its owns logo and color, when you do the design have in consideration that we are looking the experience that when you change from one product design to another the look and feel adjust to the color and logo of the product.
I am attaching:
1. Main Logo
2. Logos
3. Word Documents
You are welcome to use other icons for the each product if you want.
Target Market(s)
Independent profesional and Small and Medium Companies
Industry/Entity Type
Business and Accounting Softwares
Look and feel
Each slider illustrates characteristics of the customer's brand and the style your logo design should communicate.

```html
<!DOCTYPE html>
<html lang="es">
<head>
<meta charset="utf-8">
<title>cifra – módulos</title>
<link rel="stylesheet" href="https://fonts.googleapis.com/css2?family=Montserrat:wght@400;600;700&display=swap">
<style>
  :root{
    --ink:#222;
    --hr-green:#79b68c;
    --hr-teal:#76c7c4;
    --fin-blue:#7aaad8;
    --brand-blue:#1d5fa8;
    --label-navy:#1f4e8c;
    --ventas:#f9a825;
    --compras:#8ac5f7;
    --bancos:#8f8f8f;
    --contab:#c972db;
    --presup:#2ec995;
    --invent:#e05566;
    --nomina:#6cc7c0;
    --crm:#7a73e0;
    --tareas:#bdbdbd;
  }
  html,body{margin:0;padding:0;overflow:hidden;background:#fff}
  .canvas{width:1200px;height:387px;display:block;font-family:'Montserrat',sans-serif}
  .panel{fill:#fff;filter:url(#shadow)}
  .frame-hr{fill:none;stroke:var(--hr-teal);stroke-width:1.5}
  .frame-fin{fill:none;stroke:var(--fin-blue);stroke-width:1.5}
  .pill{fill:#fff}
  .brand-name{font-family:'Montserrat',sans-serif;font-weight:700;font-size:30px;fill:var(--brand-blue)}
  .brand-dot{fill:var(--brand-blue)}
  .hex-green{fill:var(--hr-green)}
  .hex-teal{fill:var(--hr-teal)}
  .hex-label{font-weight:600;font-size:11px;fill:#fff;text-anchor:middle}
  .hr-box{fill:#fff;stroke:var(--hr-teal);stroke-width:2}
  .hr-copy{font-size:10.4px;fill:var(--hr-green)}
  .icon-w{fill:#fff}
  .icon-ws{fill:none;stroke:#fff;stroke-width:3}
  .mod-hex{fill:#fff;stroke-width:2}
  .mod-label{font-weight:700;fill:var(--label-navy);text-anchor:middle}
  .mod-copy{font-size:8.2px;fill:#fff}
  .caption{font-size:16.5px;fill:var(--ink)}
</style>
</head>
<body>
<svg class="canvas" viewBox="0 0 2576 831" xmlns="http://www.w3.org/2000/svg">
  <defs>
    <filter id="shadow" x="-2%" y="-2%" width="104%" height="106%">
      <feDropShadow dx="0" dy="2" stdDeviation="4" flood-color="#000" flood-opacity="0.18"/>
    </filter>
    <linearGradient id="hrGrad" x1="0" y1="0" x2="0" y2="1">
      <stop offset="0" stop-color="#7ecac6"/>
      <stop offset="1" stop-color="#78b88c"/>
    </linearGradient>
  </defs>

  <!-- Human resources panel -->
  <g class="hr">
    <rect class="panel" x="26" y="27" width="1249" height="701"/>
    <rect class="frame-hr" x="40" y="39" width="1222" height="676"/>
    <polygon points="26,27 330,200 330,555 26,728" fill="url(#hrGrad)"/>
    <rect class="pill" x="84" y="348" width="188" height="58" rx="29"/>
    <circle class="brand-dot" cx="132" cy="377" r="12"/>
    <text class="brand-name" x="152" y="388">cifra</text>

    <rect class="hr-box" x="858" y="85" width="325" height="64"/>
    <text class="hr-copy"><tspan x="875" y="104" textLength="292" lengthAdjust="spacing">Automatice los cálculos de la nómina para salarios,</tspan><tspan x="875" y="120" textLength="292" lengthAdjust="spacing">deducciones, impuestos y otras formas de</tspan><tspan x="875" y="136">compensación, en base a la legislación del país.</tspan></text>
    <rect class="hr-box" x="421" y="215" width="325" height="64"/>
    <text class="hr-copy"><tspan x="443" y="234" textLength="292" lengthAdjust="spacing">Monitorea y genere registros de horas por cada</tspan><tspan x="443" y="250" textLength="292" lengthAdjust="spacing">empleado, en los que se incluye la fecha de inicio y</tspan><tspan x="443" y="266">de finalización de cada tarea.</tspan></text>
    <rect class="hr-box" x="858" y="345" width="325" height="64"/>
    <text class="hr-copy"><tspan x="875" y="364" textLength="292" lengthAdjust="spacing">Alinee su mano de obra con los objetivos de la</tspan><tspan x="875" y="380" textLength="292" lengthAdjust="spacing">organización y de seguimiento a los indicadores</tspan><tspan x="875" y="396">clave de desempeño de los empleados.</tspan></text>
    <rect class="hr-box" x="421" y="475" width="325" height="64"/>
    <text class="hr-copy"><tspan x="443" y="502" textLength="292" lengthAdjust="spacing">Optimize la contratación al simplificarla y hacerlo</tspan><tspan x="443" y="518">transparente, intuitivo e interactivo.</tspan></text>
    <rect class="hr-box" x="858" y="605" width="325" height="64"/>
    <text class="hr-copy"><tspan x="875" y="624" textLength="292" lengthAdjust="spacing">Empodera a los empleados para que gestionen</tspan><tspan x="875" y="640" textLength="292" lengthAdjust="spacing">sus actividades referentes a la administración de</tspan><tspan x="875" y="656">RRHH.</tspan></text>

    <polygon class="hex-green" points="802,52 858,84.5 858,149.5 802,182 746,149.5 746,84.5"/>
    <polygon class="hex-teal" points="802,182 858,214.5 858,279.5 802,312 746,279.5 746,214.5"/>
    <polygon class="hex-green" points="802,312 858,344.5 858,409.5 802,442 746,409.5 746,344.5"/>
    <polygon class="hex-teal" points="802,442 858,474.5 858,539.5 802,572 746,539.5 746,474.5"/>
    <polygon class="hex-green" points="802,572 858,604.5 858,669.5 802,702 746,669.5 746,604.5"/>

    <g class="icon-nomina">
      <circle class="icon-w" cx="802" cy="89" r="7"/>
      <circle class="icon-w" cx="784" cy="98" r="5"/>
      <circle class="icon-w" cx="820" cy="98" r="5"/>
      <rect class="icon-w" x="792" y="98" width="20" height="30" rx="4"/>
      <rect class="icon-w" x="775" y="106" width="14" height="22" rx="3"/>
      <rect class="icon-w" x="815" y="106" width="14" height="22" rx="3"/>
    </g>
    <text class="hex-label" x="802" y="147">Nómina</text>

    <g class="icon-asistencia">
      <circle class="icon-w" cx="802" cy="231" r="15"/>
      <rect class="icon-w" x="796" y="244" width="12" height="14" rx="2"/>
    </g>
    <text class="hex-label" x="802" y="277">Asistencia</text>

    <g class="icon-evaluacion">
      <rect class="icon-w" x="781" y="370" width="8" height="12"/>
      <rect class="icon-w" x="792" y="362" width="8" height="20"/>
      <rect class="icon-w" x="803" y="355" width="8" height="27"/>
      <rect class="icon-w" x="814" y="348" width="8" height="34"/>
      <path class="icon-ws" d="M780 356 L824 340"/>
    </g>
    <text class="hex-label"><tspan x="802" y="399">Evaluación de</tspan><tspan x="802" y="413">Desempeño</tspan></text>

    <g class="icon-contrataciones">
      <circle class="icon-ws" cx="793" cy="490" r="11" stroke-width="6"/>
      <circle class="icon-ws" cx="818" cy="510" r="6" stroke-width="4"/>
    </g>
    <text class="hex-label" x="802" y="537">Contrataciones</text>

    <g class="icon-portal">
      <rect class="icon-w" x="781" y="597" width="18" height="18" rx="2"/>
      <rect class="icon-w" x="803" y="597" width="18" height="18" rx="2"/>
      <rect class="icon-w" x="781" y="619" width="18" height="18" rx="2"/>
      <rect class="icon-w" x="803" y="619" width="18" height="18" rx="2"/>
    </g>
    <text class="hex-label"><tspan x="802" y="660">Portal Auto</tspan><tspan x="802" y="674">Servicio</tspan></text>
  </g>

  <!-- Finance panel -->
  <g class="finance">
    <rect class="panel" x="1301" y="27" width="1249" height="701"/>
    <rect class="frame-fin" x="1315" y="39" width="1222" height="676"/>
    <polygon points="1301,27 1605,200 1605,555 1301,728" fill="var(--fin-blue)"/>
    <rect class="pill" x="1359" y="348" width="188" height="58" rx="29"/>
    <circle class="brand-dot" cx="1407" cy="377" r="12"/>
    <text class="brand-name" x="1427" y="388">cifra</text>

    <rect x="1884" y="79" width="386" height="52" fill="var(--ventas)"/>
    <text class="mod-copy"><tspan x="1898" y="100" textLength="359" lengthAdjust="spacing">Comprende todo el ciclo de gestión de ventas y facturación al permitirle</tspan><tspan x="1898" y="113">realizar órdenes de venta, generar facturas y recibir pagos</tspan></text>
    <rect x="1884" y="147" width="386" height="52" fill="var(--compras)"/>
    <text class="mod-copy"><tspan x="1898" y="162" textLength="359" lengthAdjust="spacing">Gestione sus cuentas actuales, agregar clientes nuevos o reciba candidatos</tspan><tspan x="1898" y="175" textLength="359" lengthAdjust="spacing">convertidos. Enlace cuentas particulares con los productos o servicios que</tspan><tspan x="1898" y="188">ofrece y monitoreé los ingresos generados por cada cuenta.</tspan></text>
    <rect x="1884" y="215" width="386" height="52" fill="var(--bancos)"/>
    <text class="mod-copy"><tspan x="1898" y="236" textLength="359" lengthAdjust="spacing">Administre mejor los datos financieros por medio de la creación de mejores</tspan><tspan x="1898" y="249">presupuestos, previsiones, planes a corto y largo plazo y mucho más.</tspan></text>
    <rect x="1884" y="283" width="386" height="52" fill="var(--contab)"/>
    <text class="mod-copy"><tspan x="1898" y="304" textLength="359" lengthAdjust="spacing">Es un software intuitivo que facilita el registro y tratamiento de todas las</tspan><tspan x="1898" y="317">transacciones financieras.</tspan></text>
    <rect x="1884" y="351" width="386" height="52" fill="var(--presup)"/>
    <text class="mod-copy"><tspan x="1898" y="372" textLength="359" lengthAdjust="spacing">Este software es ideal para organizaciones pequeñas y medianas y ayuda a</tspan><tspan x="1898" y="385">los equipos a reunir todos sus datos en un solo lugar.</tspan></text>
    <rect x="1884" y="419" width="386" height="52" fill="var(--invent)"/>
    <text class="mod-copy"><tspan x="1898" y="440" textLength="359" lengthAdjust="spacing">Administre almacenes, inventarios y la cantidad y valor de los articulos de</tspan><tspan x="1898" y="453">manera mas eficiente.</tspan></text>
    <rect x="1884" y="487" width="386" height="52" fill="var(--nomina)"/>
    <text class="mod-copy"><tspan x="1898" y="508" textLength="359" lengthAdjust="spacing">Automatice los cálculos de la nómina para salarios, deducciones, impuestos</tspan><tspan x="1898" y="521">y otras formas de compensación, en base a la legislación del país.</tspan></text>
    <rect x="1884" y="555" width="386" height="52" fill="var(--crm)"/>
    <text class="mod-copy"><tspan x="1898" y="576" textLength="359" lengthAdjust="spacing">Es una solución de gestión CRM con plataforma web e integración con</tspan><tspan x="1898" y="589">ChatLine. Cotice desde CIFRA con ChatLine.</tspan></text>
    <rect x="1884" y="623" width="386" height="52" fill="var(--tareas)"/>
    <text class="mod-copy"><tspan x="1898" y="638" textLength="359" lengthAdjust="spacing">Administre las tareas internas, externas y colaborar entre equipos de trabajo</tspan><tspan x="1898" y="651" textLength="359" lengthAdjust="spacing">y sus cliente. Desde cualquiera de las aplicaciones, usted tiene acceso a</tspan><tspan x="1898" y="664">potentes herramientas para ver el estado de sus tareas.</tspan></text>

    <polygon class="mod-hex" stroke="var(--ventas)" points="1838,52 1884,78.5 1884,131.5 1838,158 1792,131.5 1792,78.5"/>
    <g fill="var(--ventas)"><rect x="1824" y="106" width="5" height="10"/><rect x="1831" y="100" width="5" height="16"/><rect x="1838" y="94" width="5" height="22"/><rect x="1845" y="88" width="5" height="28"/></g>
    <text class="mod-label" x="1838" y="131" font-size="14.5">VENTAS</text>

    <polygon class="mod-hex" stroke="var(--compras)" points="2316,120 2362,146.5 2362,199.5 2316,226 2270,199.5 2270,146.5"/>
    <rect x="2304" y="158" width="24" height="20" rx="2" fill="var(--compras)"/>
    <text class="mod-label" x="2316" y="194" font-size="13">COMPRAS</text>

    <polygon class="mod-hex" stroke="var(--bancos)" points="1838,188 1884,214.5 1884,267.5 1838,294 1792,267.5 1792,214.5"/>
    <g fill="#555"><polygon points="1826,228 1838,220 1850,228"/><rect x="1827" y="230" width="22" height="16"/></g>
    <text class="mod-label" x="1838" y="264" font-size="16">BANCOS</text>

    <polygon class="mod-hex" stroke="var(--contab)" points="2316,256 2362,282.5 2362,335.5 2316,362 2270,335.5 2270,282.5"/>
    <g fill="var(--contab)"><rect x="2306" y="291" width="7" height="7"/><rect x="2316" y="291" width="7" height="7"/><rect x="2306" y="301" width="7" height="7"/><rect x="2316" y="301" width="7" height="7"/></g>
    <text class="mod-label" x="2316" y="327" font-size="8.8">CONTABILIDAD</text>

    <polygon class="mod-hex" stroke="var(--presup)" points="1838,324 1884,350.5 1884,403.5 1838,430 1792,403.5 1792,350.5"/>
    <g fill="var(--presup)"><ellipse cx="1838" cy="366" rx="13" ry="5"/><ellipse cx="1838" cy="374" rx="13" ry="5"/><ellipse cx="1838" cy="382" rx="13" ry="5"/></g>
    <text class="mod-label" x="1838" y="396" font-size="9.2">PRESUPUESTO</text>

    <polygon class="mod-hex" stroke="var(--invent)" points="2316,392 2362,418.5 2362,471.5 2316,498 2270,471.5 2270,418.5"/>
    <rect x="2302" y="424" width="24" height="26" fill="var(--invent)"/>
    <text class="mod-label" x="2316" y="470" font-size="9">INVENTARIOS</text>

    <polygon class="mod-hex" stroke="var(--nomina)" points="1838,460 1884,486.5 1884,539.5 1838,566 1792,539.5 1792,486.5"/>
    <g fill="var(--nomina)"><circle cx="1838" cy="498" r="5"/><circle cx="1827" cy="503" r="4"/><circle cx="1849" cy="503" r="4"/><rect x="1831" y="505" width="14" height="16" rx="3"/><rect x="1821" y="509" width="11" height="12" rx="2"/><rect x="1844" y="509" width="11" height="12" rx="2"/></g>
    <text class="mod-label" x="1838" y="535" font-size="11.5">NÓMINA RH</text>

    <polygon class="mod-hex" stroke="var(--crm)" points="2316,528 2362,554.5 2362,607.5 2316,634 2270,607.5 2270,554.5"/>
    <path d="M2300 576 L2316 566 L2332 576" fill="none" stroke="var(--crm)" stroke-width="4"/>
    <text class="mod-label" x="2316" y="607" font-size="25">CRM</text>

    <polygon class="mod-hex" stroke="var(--tareas)" points="1838,596 1884,622.5 1884,675.5 1838,702 1792,675.5 1792,622.5"/>
    <rect x="1830" y="634" width="16" height="22" rx="2" fill="none" stroke="#777" stroke-width="2"/>
    <path d="M1836 646 L1841 651 L1856 628" fill="none" stroke="#777" stroke-width="2"/>
    <text class="mod-label" x="1838" y="674" font-size="14.5">TAREAS</text>
  </g>

  <text class="caption" x="33" y="791">Example of 2 graphic designs for ‘Human Resources’ and ‘Finance’. Will send the rest of designs if chosen by client.</text>
</svg>
</body>
</html>
```